Halvorsen Spa

We are a large Miami Beach spa and salon. I am still building our website but you can use it as a resource to gain a better understanding of who we are ....www.spaquillowave.com.

We offer a comprehensive list of services in hair, nails, massage, skin care, tanning, spray tanning and waxing and we offer high quality products for skin care, tanning and hair. We are open 7 days.

We would like to see a clean and simple menu that looks a lot like the one from "The Spa at Brightmere." In particular, we have a copy of a menu from their West Hollywood, CA location that is just beautiful. In the uploaded content you will see a sampling of that menu. We would like to see greys, blacks, silvers, whites and warm colors like reds and oranges. We specifically attempt to remain gender neutral so that we don't attract only girls (with pink colors and flowers etc). The final design should convey a simple, clean, friendly environment and the final product should be sized such that it is 1.) portable and 2.) inexpensive to print. We will be running thousands of these at a time so cost of printing is a consideration.

The booklet consists of two parts: one part is the standard menu with descriptions of services and products and photos etc (think of this as the sales piece that convinces a potential customer to visit) and will be stapled together like you would expect a small menu to be and should resemble the Brightmere menu. The prices should not be included in this part of the booklet that will be printed and stapled. The other part is a single insert and is removable and replaceable. I want this removable insert placed in the last page of the book in a folder pocket or something else that you can think of so that when it's time to change prices here that I am not throwing away all of the booklets....I am only replacing the inserts at the end of the menu booklet. Please design this single page insert so that should a customer remove it from the booklet and keep it, that it stands alone with our name, logo, website and phone number. This page can and probably will have to be 2 sided.

At the back of the booklet, I also want the polices to be printed in one page (think fine print in any sort of business dealing.)

With regard to the look and feel slider of economical v upmarket...we definitely want to convey we deliver upmarket services at reasonable prices. Think, world class services and products at reasonable, everyday prices.

With regard to the uploaded files:
I uploaded both EPS and TIF formats. The colors in those files are not the palette we want at all. The colors we want use for the circular logo must match the standard colors as depicted in the uploaded file "Halvorsentanrooms"

Target Market(s)

The target market is the average 20-35 year old in Miami Beach that cares about their appearance. The range of clientele is quite diverse.

Industry/Entity Type

Environment

Requirements
Must have
• It must have elegant and simple photographs that relate to the services being offered. We are selling a service set and an environment...so this menu should be reflect that goal. The logo should be repeated often throughout the book but in subtle ways.

Stock photos are fine as long as they don't seem obviously stock.

Should not have
• Nothing buddha like. Nothing themed. It should be all inclusive and not seek to identify with any particular group or gender.

Nothing that fits the stereotype of "Miami Beach." We want to represent ourselves in the same category as the best spas in the world because we moving everything we do in that direction. Think class!

```html
<!DOCTYPE html>
<html lang="en">
<head>
<meta charset="utf-8">
<title>Halvorsen Spa – Massage Menu</title>
<link rel="stylesheet" href="https://fonts.googleapis.com/css2?family=Source+Sans+3:wght@300;400;600&family=Mulish:wght@700&display=swap">
<style>
  :root {
    --paper: #ffffff;
    --terracotta: #cc8558;
    --terracotta-deep: #b2744a;
    --ink-light: #ffffff;
    --title-grey: #6d6a68;
    --body-dark: #3a3431;
    --frame: rgba(160, 152, 146, 0.75);
    --photo-sky: #e9f1f6;
    --photo-skin: #e2b89a;
    --photo-warm: #c99574;
    --band: rgba(255, 255, 255, 0.55);
  }
  * { box-sizing: border-box; margin: 0; padding: 0; }
  html, body { width: 1200px; height: 600px; overflow: hidden; background: var(--paper); }
  .spread {
    position: relative;
    width: 1200px;
    height: 600px;
    overflow: hidden;
    font-family: "Source Sans 3", "Myriad Pro", sans-serif;
  }
  .spread__art { position: absolute; inset: 0; }

  .cover-title {
    position: absolute;
    left: 31px;
    top: 468px;
    font-weight: 300;
    font-size: 43px;
    letter-spacing: 9px;
    color: var(--title-grey);
    line-height: 1;
  }
  .cover-intro {
    position: absolute;
    left: 318px;
    top: 467px;
    width: 262px;
    font-family: "Mulish", Verdana, sans-serif;
    font-weight: 700;
    font-size: 7.6px;
    line-height: 11px;
    letter-spacing: 0.9px;
    color: var(--body-dark);
  }

  .menu {
    position: absolute;
    left: 709px;
    top: 0;
    width: 440px;
    height: 600px;
    color: var(--ink-light);
  }
  .menu__head,
  .price-row {
    display: grid;
    grid-template-columns: 263px 75px 1fr;
  }
  .menu__head {
    position: absolute;
    top: 66px;
    left: 0;
    width: 100%;
    font-size: 11.5px;
  }
  .treatment { position: absolute; left: 0; width: 100%; }
  .treatment--swedish { top: 91px; }
  .treatment--aroma { top: 240px; }
  .treatment--deep { top: 374px; }
  .treatment__name { font-size: 11.5px; font-weight: 400; line-height: 15px; }
  .treatment__desc { font-size: 9.3px; line-height: 13.5px; width: 432px; margin-bottom: 13px; }
  .price-row { font-size: 9.3px; line-height: 13.6px; }

  .brand {
    position: absolute;
    left: 1050px;
    top: 518px;
    width: 120px;
    text-align: center;
    color: var(--ink-light);
  }
  .brand__mark {
    width: 30px;
    height: 30px;
    border-radius: 50%;
    border: 1.5px solid var(--ink-light);
    margin: 0 auto 6px;
  }
  .brand__name {
    font-size: 14px;
    font-weight: 400;
    letter-spacing: 1.5px;
  }
</style>
</head>
<body>
<main class="spread">
  <svg class="spread__art" width="1200" height="600" viewBox="0 0 1200 600" aria-hidden="false">
    <defs>
      <linearGradient id="photoTone" x1="0" y1="0" x2="0.4" y2="1">
        <stop offset="0" stop-color="var(--photo-sky)"/>
        <stop offset="0.35" stop-color="#f0dccb"/>
        <stop offset="0.6" stop-color="var(--photo-skin)"/>
        <stop offset="1" stop-color="#f3e6da"/>
      </linearGradient>
      <linearGradient id="panelTone" x1="0" y1="0" x2="1" y2="1">
        <stop offset="0" stop-color="var(--terracotta)"/>
        <stop offset="1" stop-color="var(--terracotta-deep)"/>
      </linearGradient>
    </defs>
    <rect class="hero-photo" x="0" y="0" width="700" height="600" fill="url(#photoTone)" role="img" aria-label="Photograph: a client lying face down receiving a relaxing shoulder massage"/>
    <rect class="hero-band" x="0" y="432" width="700" height="168" fill="var(--band)"/>
    <path class="menu-panel" d="M665 0 H1200 V600 H551 C622 590 665 530 665 427 Z" fill="url(#panelTone)"/>
    <rect class="page-frame" x="20" y="18" width="1162" height="563" fill="none" stroke="var(--frame)" stroke-width="1.5"/>
  </svg>

  <h1 class="cover-title">MASSAGE</h1>
  <p class="cover-intro">consuli coris noresseNonfes Ad accientrum publibus ina ne iam stantes ilistractus, con invenitius nonde-trur quem dem diendee straelicum confec recivisqua cotilici cons etemorudam condit. Locturs in sa num</p>

  <section class="menu">
    <div class="menu__head"><span>MASSAGE</span><span>Residents</span><span>Hotel Guests</span></div>

    <article class="treatment treatment--swedish">
      <h2 class="treatment__name">SWEDISH MASSAGE</h2>
      <p class="treatment__desc">A traditional massage that seeks to promote relaxation, enhance circulation and ease tension throughout the body through the use of gentle pressure. The massage may incorporate effleurage, kneading, friction or stretching, depending upon your needs.</p>
      <div class="price-row"><span>The 30-Minute Swedish</span><span>$ 59.00</span><span>$70.00</span></div>
      <div class="price-row"><span>The 60-Minute Swedish</span><span>$ 89.00</span><span>$105.00</span></div>
      <div class="price-row"><span>The 90-Minute Swedish</span><span>$129.00</span><span>$150.00</span></div>
      <div class="price-row"><span>The 120-Minute Swedish</span><span>$169.00</span><span>$225.00</span></div>
    </article>

    <article class="treatment treatment--aroma">
      <h2 class="treatment__name">AROMATHERAPY</h2>
      <p class="treatment__desc">The sense of smell is the most primitive of senses. It is directly connected to the limbic system, from which emotions and memories originate. Our massage therapists will take the time to personalize your sensory journey that will either leave you either energized and refreshed or at peace and balanced- the choice is yours.</p>
      <div class="price-row"><span>The 75-Minute Sensory Journey</span><span>$119.00</span><span>$135.00</span></div>
      <div class="price-row"><span>The 105-Minute Sensory Journey</span><span>$159.00</span><span>$185.00</span></div>
    </article>

    <article class="treatment treatment--deep">
      <h2 class="treatment__name">DEEP TISSUE MASSAGE</h2>
      <p class="treatment__desc">A type of massage that aims to reduce tension and stress at the deeper tissues and structures of muscle and fascia through the slower application of deep pressure, especially in and around areas of tension and pain.</p>
      <div class="price-row"><span>The 30-Minute Deep Tissue</span><span>$ 69.00</span><span>$ 80.00</span></div>
      <div class="price-row"><span>The 60-Minute Deep Tissue</span><span>$ 99.00</span><span>$120.00</span></div>
      <div class="price-row"><span>The 90-Minute Deep Tissue</span><span>$139.00</span><span>$180.00</span></div>
      <div class="price-row"><span>The 120-Minute Deep Tissue</span><span>$189.00</span><span>$240.00</span></div>
    </article>
  </section>

  <div class="brand">
    <div class="brand__mark"></div>
    <p class="brand__name">Halvorsen Spa</p>
  </div>
</main>
</body>
</html>
```